Brisk Tails Dog Behaviour, Training and Natural Healthcare Website

Hey there,
I need a webpage designed for my new business. It needs to be something authentic, new, fresh and representative of my business ethos. I operate out of Newcastle, NSW. I believe my job is to keep dogs alive and in their home by promoting communication and connection between dogs and their owners. This can't be achieved through training and behaviour alone. Nutritional guidance and environmental adaptation are often needed to complete the package and increase the success rate for these programs. I provide practical services such as walking coaching, nutrition profiling, behavioural modification, puppy minding, board and train programs for puppies and young dogs, training, basic and complex skills training, physical therapies and natural healthcare options. In effect taking care of the whole dog.
My motto is = Happy dogs, happy owners.
My catch cry is = promoting communication and connection between dogs and their owners.

I have in mind pages that can also link to other pages when an icon is clicked. I need a homepage, sections to explain what each of my services do (4 - which could be independent pages so I can attach photos) and a gallery. I want to have multi page function, an online capability for future retail, ability to amend and update content myself, an online booking and payment facility. My interests lie in I have seen many successes via and environmental modifications.
I've attached the logo which features prominently on my business card and Chatterlane page. The corporate colours are Blue with a splash of red and white. The dog being held in the healing hands must feature.

Thanks!

Target Market(s)

Australian Pet Dog Owners

Colors
0355a3
ec1f27
ffffff

Requirements
Must have
• The business colours (blue with a splash of red and white), the dog in the healing hands
Should not have
• Pawprints or cartoon animals

```html
<!DOCTYPE html>
<html lang="en">
<head>
<meta charset="utf-8">
<title>Brisk Tails – Dog Behaviour, Training and Natural Healthcare</title>
<link href="https://fonts.googleapis.com/css2?family=Merriweather:ital,wght@0,400;0,700;1,400&family=Open+Sans:ital,wght@0,400;0,600;1,400&display=swap" rel="stylesheet">
<style>
  :root {
    --blue: #0355a3;
    --red: #ec1f27;
    --white: #ffffff;
    --ink: #333333;
    --text: #777777;
    --rule: #e2e2e2;
    --footer: #3b3b3b;
    --footer-text: #dddddd;
  }
  * { margin: 0; padding: 0; box-sizing: border-box; }
  html, body { width: 802px; height: 1200px; overflow: hidden; background: var(--white); }
  body { position: relative; font-family: "Open Sans", Arial, sans-serif; color: var(--text); }
  .abs { position: absolute; }

  /* header */
  .brand-badge {
    left: 75px; top: 22px; width: 94px; height: 94px; border-radius: 50%;
    background: radial-gradient(circle at 50% 35%, #1f7fd6, var(--blue) 70%);
    border: 3px solid var(--white); box-shadow: 0 2px 5px rgba(0,0,0,.35);
    z-index: 3; display: flex; align-items: center; justify-content: center;
  }
  .brand-badge span { font-family: "Merriweather", Georgia, serif; font-size: 8px; font-weight: 700; color: var(--white); letter-spacing: .3px; }
  .main-nav { top: 37px; left: 0; width: 802px; font-family: "Merriweather", Georgia, serif; font-size: 7.5px; color: #555; text-transform: uppercase; }
  .main-nav a { position: absolute; color: inherit; text-decoration: none; white-space: nowrap; }
  .main-nav a.active { color: var(--blue); }

  /* hero */
  .hero { left: 66px; top: 86px; width: 669px; height: 354px;
    background:
      radial-gradient(ellipse 30% 45% at 78% 45%, rgba(226,214,190,.85), rgba(226,214,190,0) 70%),
      radial-gradient(ellipse 25% 30% at 42% 85%, rgba(240,232,214,.8), rgba(240,232,214,0) 70%),
      linear-gradient(180deg, #c9a24a 0%, #a48a4c 45%, #8d7d52 75%, #8a7a4a 100%); }
  .hero-shadow { left: 90px; top: 438px; width: 620px; height: 22px;
    background: radial-gradient(ellipse at 50% 0%, rgba(0,0,0,.28), rgba(0,0,0,0) 70%); }
  .hero-title { left: 90px; top: 203px; font-family: "Merriweather", Georgia, serif; font-weight: 400; font-size: 33px; color: var(--white); letter-spacing: .5px; }
  .hero-copy { left: 90px; top: 248px; width: 275px; font-size: 8.8px; line-height: 17px; color: var(--white); }
  .hero-dots { left: 90px; top: 403px; display: flex; gap: 2px; }
  .hero-dots i { width: 6px; height: 6px; background: var(--white); display: block; }
  .hero-dots i.on { background: var(--blue); }

  /* section headings */
  .section-title { left: 66px; width: 667px; display: flex; align-items: center; gap: 6px;
    font-family: "Merriweather", Georgia, serif; font-weight: 400; font-size: 15px; color: var(--ink); white-space: nowrap; }
  .section-title::after { content: ""; flex: 1; height: 1px; background: var(--rule); }

  .body-copy { font-size: 8.8px; line-height: 15px; color: var(--text); white-space: nowrap; }

  .welcome-photo { left: 66px; top: 527px; width: 138px; height: 138px; border-radius: 50%;
    background: linear-gradient(180deg, #e4ecef 0%, #c9d6d8 35%, #8aa35a 62%, #6f9234 100%);
    border: 2px solid #fff; box-shadow: 0 0 0 1px #ddd; }
  .btn-more { left: 226px; top: 638px; width: 89px; height: 31px; background: var(--blue);
    color: var(--white); font-family: "Merriweather", Georgia, serif; font-size: 11px;
    display: flex; align-items: center; justify-content: center; text-decoration: none; }

  /* services */
  .service-photo { top: 786px; width: 96px; height: 96px; border-radius: 50%; border: 2px solid #fff; box-shadow: 0 0 0 1px #ccc; }
  .service-name { top: 900px; font-family: "Merriweather", Georgia, serif; font-size: 9px; font-weight: 700; color: var(--blue); white-space: nowrap; }
  .zoom { left: 672px; top: 820px; width: 28px; height: 28px; border-radius: 50%; background: var(--white); }

  /* news */
  .news-month { top: 987px; font-family: "Merriweather", Georgia, serif; font-size: 12.5px; color: var(--blue); line-height: 18px; }
  .news-divider { top: 989px; width: 1px; height: 30px; background: var(--rule); }
  .news-head { top: 996px; font-family: "Merriweather", Georgia, serif; font-style: italic; font-size: 9.5px; color: #666; white-space: nowrap; }
  .news-text { top: 1029px; }
  .news-link { top: 1069px; font-size: 9px; color: var(--blue); text-decoration: none; }

  /* footer */
  .site-footer { left: 0; top: 1123px; width: 802px; height: 77px; background: var(--footer); }
  .footer-nav { left: 66px; top: 1141px; font-size: 8.8px; color: var(--footer-text); display: flex; gap: 15px; white-space: nowrap; }
  .footer-nav .sep { color: #bbb; }
  .copyright { left: 66px; top: 1173px; font-size: 8.8px; color: var(--footer-text); }
  .social { top: 1140px; width: 19px; height: 19px; border-radius: 50%; background: var(--white);
    display: flex; align-items: center; justify-content: center;
    font-family: "Open Sans", Arial, sans-serif; font-size: 8.5px; font-weight: 600; color: var(--footer); text-decoration: none; }
</style>
</head>
<body>

<header>
  <div class="abs brand-badge"><span>BRISKTAILS</span></div>
  <nav class="abs main-nav">
    <a class="active" style="left:357px">Home</a>
    <a style="left:414px">About Us</a>
    <a style="left:488px">Services</a>
    <a style="left:560px">Gallery</a>
    <a style="left:630px">Blog</a>
    <a style="left:684px">Contact Us</a>
  </nav>
</header>

<section>
  <div class="abs hero" role="img" aria-label="Photo of a woman in an autumn park feeding a treat to a labrador on a red lead"></div>
  <div class="abs hero-shadow"></div>
  <h1 class="abs hero-title">BRISK TAILS</h1>
  <p class="abs hero-copy">Solum fugit voluptatibus mea ut, ad augue tritani interpretaris vim. Praesent adversarium mea an, ne equidem menandri sed, viris nobis te pro.</p>
  <div class="abs hero-dots"><i class="on"></i><i></i><i></i><i></i></div>
</section>

<section>
  <h2 class="abs section-title" style="top:490px">WELCOME TO BRISK TAILS</h2>
  <div class="abs welcome-photo" role="img" aria-label="Photo of a girl playing with a jumping dog in a grassy field"></div>
  <p class="abs body-copy" style="left:226px;top:524px">Solum fugit voluptatibus mea ut, ad augue tritani interpretaris vim. Praesent adversarium mea an, ne equidem menandri<br>sed, viris nobis te pro. Pro in assum cetero eligendi, ad mea noster persius nostrud. Quem detraxit ex nam, erant graece<br>vel ne. Ut nec malis movet labore, cu vix congue tincidunt.</p>
  <p class="abs body-copy" style="left:226px;top:577px">Solum fugit voluptatibus mea ut, ad augue tritani interpretaris vim. Praesent adversarium mea an, ne equidem menandri<br>sed, viris nobis te pro. Pro in assum cetero eligendi, ad mea noster persius nostrud. Quem detraxit ex nam, erant graece<br>vel ne. Ut nec malis movet labore, cu vix congue tincidunt.</p>
  <a class="abs btn-more">MORE INFO</a>
</section>

<section>
  <h2 class="abs section-title" style="top:709px">OUR SERVICES</h2>
  <p class="abs body-copy" style="left:66px;top:740px">Has dolor evertitur ea, oblique laoreet menandri id his. Rebum suscipit sadipscing eum an, ad tota justo vel, mel mutat fugit dissentiunt ne. Mei id debet pla-<br>tonem. Ei pri fugit antiopam qualisque, Has dolor evertitur ea, oblique laoreet menandri id his. Rebum suscipit sadipscing eum an, ad tota just.</p>

  <div class="abs service-photo" style="left:67px;background:linear-gradient(160deg,#8fa65a 0%,#c8944a 40%,#d4b23a 65%,#4f6e2a 100%)" role="img" aria-label="Photo of a dog leaping over an agility hurdle"></div>
  <div class="abs service-photo" style="left:253px;background:linear-gradient(120deg,#6b5236 0%,#e0bd8c 40%,#d8a55c 65%,#2e2622 100%)" role="img" aria-label="Photo of a woman hugging a golden retriever"></div>
  <div class="abs service-photo" style="left:446px;background:linear-gradient(180deg,#5f7f34 0%,#d9ad6e 45%,#c99a58 60%,#6e9a36 100%)" role="img" aria-label="Photo of a labrador puppy lying in the grass"></div>
  <div class="abs service-photo" style="left:638px;background:linear-gradient(180deg,#3a3626 0%,#5b4e38 45%,#2f4a22 75%,#24361a 100%)" role="img" aria-label="Photo of a running terrier with a ball"></div>
  <div class="abs zoom">
    <svg width="28" height="28" viewBox="0 0 28 28"><circle cx="12.5" cy="12.5" r="4.5" fill="none" stroke="#0355a3" stroke-width="2"/><line x1="16" y1="16" x2="19.5" y2="19.5" stroke="#0355a3" stroke-width="2.4" stroke-linecap="round"/></svg>
  </div>

  <div class="abs service-name" style="left:67px">WALKING COACHING</div>
  <div class="abs service-name" style="left:249px">NUTRITION PROFILING</div>
  <div class="abs service-name" style="left:457px">PUPPY MINDING</div>
  <div class="abs service-name" style="left:635px">PHYSICAL THERAPIES</div>
</section>

<section>
  <h2 class="abs section-title" style="top:956px">LATEST NEWS</h2>

  <article>
    <div class="abs news-month" style="left:66px">MAR<br>02</div>
    <div class="abs news-divider" style="left:104px"></div>
    <div class="abs news-head" style="left:113px">Solum fugit voluptatibus mea</div>
    <p class="abs body-copy news-text" style="left:66px">Has dolor evertitur ea, oblique laoreet me-<br>nandri id his. Rebum suscipit.</p>
    <a class="abs news-link" style="left:66px">[ More Info ]</a>
  </article>
  <article>
    <div class="abs news-month" style="left:307px">MAR<br>09</div>
    <div class="abs news-divider" style="left:345px"></div>
    <div class="abs news-head" style="left:354px">Solum fugit voluptatibus mea</div>
    <p class="abs body-copy news-text" style="left:307px">Has dolor evertitur ea, oblique laoreet me-<br>nandri id his. Rebum suscipit.</p>
    <a class="abs news-link" style="left:307px">[ More Info ]</a>
  </article>
  <article>
    <div class="abs news-month" style="left:552px">MAR<br>30</div>
    <div class="abs news-divider" style="left:590px"></div>
    <div class="abs news-head" style="left:599px">Solum fugit voluptatibus mea</div>
    <p class="abs body-copy news-text" style="left:552px">Has dolor evertitur ea, oblique laoreet me-<br>nandri id his. Rebum suscipit.</p>
    <a class="abs news-link" style="left:552px">[ More Info ]</a>
  </article>
</section>

<footer>
  <div class="abs site-footer"></div>
  <nav class="abs footer-nav">
    <span>Home</span><span class="sep">/</span><span>About Us</span><span class="sep">/</span><span>Services</span><span class="sep">/</span><span>Gallery</span><span class="sep">/</span><span>Blog</span><span class="sep">/</span><span>Contact Us</span>
  </nav>
  <p class="abs copyright">Copyright @ 2014 BriskTails.All Rights Reserved.</p>
  <a class="abs social" style="left:627px" aria-label="Chirpset">C</a>
  <a class="abs social" style="left:650px" aria-label="Orbitring">O</a>
  <a class="abs social" style="left:672px" aria-label="Snapboard">S</a>
  <a class="abs social" style="left:695px" aria-label="Chatterlane">C</a>
  <a class="abs social" style="left:717px" aria-label="Workweave">W</a>
</footer>

</body>
</html>
```